Australian Craft Distillery needs poster layout for its awesome Manifesto

Tall Finch's a small craft distillery based in the Brook Flats of Western Australia producing award-winning vodkas and gin. Check out our website www.tallfinchs-example.com.au to get a feel for our design aesthetic, especially from our bottle design. We are "Small Batch Liquors - Out of the Brook Flats". Everything we do reflects that.
We have a manifesto - The Tall Finch's Manifesto -that we proudly display in our tasting room, and was used as a basis for an artwork in our entry.
We've had a number of customers ask to buy a poster of the manifesto (attached) so I want to commission a more professional design than the current layout which was put together in Word! (yes I know, I'm sorry, I did move it into Illustrator later).
I think the text flows in a sequential order so I'm looking for a design that you read from start to finish rather than a random collection of statements. I'd like to include our logo in the design somewhere but it doesn't have to be front and centre. There is a secondary logo device as well - the interlocked T and F on the label which could be used. I'm assuming the print will be simple black on either a plain background or a "craft background" similar to the labels. Our current fonts are SchmutzICG for text and VeneerTwo for headings. The label uses Haymaker and Gin-Rough.
Print size will be A3 (prefer the design to be to this proportion and portrait orientation) and bigger up to A1. We'll print the final design on the back of t-shirts for staff as well. If I was going to sum up our style in a couple of words it would be "intelligently irreverent" Have fun with this, I certainly did writing it!

```html
<!DOCTYPE html>
<html lang="en">
<head>
<meta charset="utf-8">
<title>The Tall Finch's Manifesto</title>
<link rel="stylesheet" href="https://fonts.googleapis.com/css2?family=Anton&family=Oswald:wght@700&family=Special+Elite&display=swap">
<style>
  :root {
    --kraft: #c89f72;
    --kraft-light: #d4ae83;
    --ink: #161210;
    --paper-text: #d9b98f;
  }
  * { box-sizing: border-box; margin: 0; padding: 0; }
  html, body { width: 849px; height: 1200px; overflow: hidden; background: var(--kraft); }
  .poster {
    position: relative;
    width: 849px; height: 1200px;
    background: radial-gradient(ellipse at 50% 40%, var(--kraft-light), var(--kraft) 75%);
    border: 16px solid var(--ink);
    color: var(--ink);
    font-family: "Special Elite", "Courier New", monospace;
  }
  .poster__inner {
    position: absolute; inset: 12px;
    border: 2px solid var(--ink);
    border-radius: 6px;
    padding: 22px 36px 20px;
    display: flex; flex-direction: column; align-items: center;
  }
  .brand {
    display: flex; align-items: center; gap: 8px;
    font-family: "Special Elite", monospace; font-size: 15px;
    letter-spacing: 1px;
  }
  .brand__dot { width: 12px; height: 12px; border-radius: 50%; background: var(--ink); }
  .title__pre {
    margin-top: 14px;
    font-family: "Oswald", sans-serif; font-weight: 700;
    font-size: 36px; letter-spacing: 1px; line-height: 1;
  }
  .title__main {
    font-family: "Anton", sans-serif;
    font-size: 118px; line-height: 1.02; letter-spacing: 1px;
  }
  .subtitle { font-size: 19px; margin-top: 2px; }
  .section { width: 100%; margin-top: 22px; }
  .section__head {
    display: flex; align-items: center; gap: 0; margin-bottom: 14px;
  }
  .section__rule { flex: 1; height: 0; border-top: 2px solid var(--ink); }
  .section__rule--double { border-top: 4px double var(--ink); }
  .section__label {
    background: var(--ink); color: var(--paper-text);
    font-family: "Oswald", sans-serif; font-weight: 700;
    font-size: 22px; letter-spacing: 2px;
    padding: 3px 18px; line-height: 1.2;
  }
  .section__body { font-size: 19.5px; line-height: 1.55; }
  .section__body--centered { text-align: center; }
  .section__body--justified { text-align: justify; }
</style>
</head>
<body>
<main class="poster">
  <div class="poster__inner">
    <div class="brand"><span class="brand__dot"></span><span>Tall Finch's</span></div>
    <h1 class="title">
      <div class="title__pre">THE TALL FINCH'S</div>
      <div class="title__main">MANIFESTO</div>
    </h1>
    <p class="subtitle">(our thoughts on life, a.k.a. how to be better)</p>

    <section class="section">
      <div class="section__head"><span class="section__rule section__rule--double"></span><span class="section__label">FIRST</span><span class="section__rule section__rule--double"></span></div>
      <p class="section__body section__body--centered">Work Smart • Love Hard • Play Often • Sleep More • Stay Present • Be Local • Embrace Silly • Get Dirty (but) Stay Clean • Laugh • Cry • Run • Dance • Sing • Stop That (and) Slow down •</p>
    </section>

    <section class="section">
      <div class="section__head"><span class="section__rule section__rule--double"></span><span class="section__label">THEN</span><span class="section__rule section__rule--double"></span></div>
      <p class="section__body section__body--justified">• Celebrate others success • Don't be shit • Have one thing you are awesome at • Get off your phone • Show some fucking passion • Make something • Making money doesn't count • Making babies does • Never stop exploring, never stop learning, share that with others • We all fuck up. Make good, learn, be better and move on • Life is far too short, squeeze every drop out of it •and, of course ... • Drink better •</p>
    </section>

    <section class="section">
      <div class="section__head"><span class="section__rule section__rule--double"></span><span class="section__label">AND FINALLY</span><span class="section__rule section__rule--double"></span></div>
      <p class="section__body section__body--justified">• Sometimes you just won't understand • An argument is not a fight • You are not as important as you think • You are more loved than you think • Its ok to do things alone • Its ok not to be busy • There is no good reason to do a half arsed job • Teaching is the best way of learning • The past is important, what you do next is much more so • Change is inevitable, roll with it • Success is whatever you decide it to be •</p>
    </section>
  </div>
</main>
</body>
</html>
```